Design the app for the next NestLoop

We need a cutting edge, super UX-intuitive, design for a global parking app called Vamo.
- Homescreen and website have been finalised already (see attached pdf)
- Wireframed screens for the concepts we need have been provided in the attached pdf
- We need some really nice icons for parking space types, etc
- Needs to be very, very intuitive to use and navigate.
References: NestLoop app & Zolt app, for their simplicity of use
Updates
Project Deadline Extended
Reason: A few designers have requested that we extend this deadline. So here you go.
Industry/Entity Type
Parking
Look and feel
Each slider illustrates characteristics of the customer's brand and the style your logo design should communicate.

```html
<!DOCTYPE html>
<html lang="en">
<head>
<meta charset="utf-8">
<title>Vamo – Home Screen Mocks</title>
<link href="https://fonts.googleapis.com/css2?family=Montserrat:wght@600;700&family=Open+Sans:wght@400;600&family=Quicksand:wght@400;500&display=swap" rel="stylesheet">
<style>
  :root {
    --bg-left: #2b8199;
    --bg-right: #45a8dd;
    --screen-dark: #17161b;
    --screen-cyan: #34c1e4;
    --status-bg: #efefef;
    --status-ink: #111111;
    --coral: #f05d63;
    --sky: #3aa8de;
    --ink: #0d0d0f;
    --white: #ffffff;
  }
  * { box-sizing: border-box; margin: 0; padding: 0; }
  html, body { width: 1138px; height: 1200px; overflow: hidden; }
  body { position: relative; font-family: "Open Sans", sans-serif; }

  .backdrop { position: absolute; top: 0; height: 1200px; }
  .backdrop--left { left: 0; width: 568px; background: var(--bg-left); }
  .backdrop--right { left: 568px; width: 570px; background: var(--bg-right); }

  .screen {
    position: absolute; top: 204px; width: 386px; height: 690px; overflow: hidden;
  }
  .screen--dark { left: 88px; background: var(--screen-dark); }
  .screen--cyan { left: 658px; background: var(--screen-cyan); height: 686px; }

  .status-bar {
    position: absolute; top: 0; left: 0; width: 100%; height: 35px;
    background: var(--status-bg); color: var(--status-ink);
    font-family: "Open Sans", sans-serif; font-size: 14px; font-weight: 600;
    display: flex; align-items: center; justify-content: space-between; padding: 0 8px;
  }
  .status-bar__left, .status-bar__right { display: flex; align-items: center; gap: 4px; }
  .status-bar__time { position: absolute; left: 0; right: 0; text-align: center; pointer-events: none; }
  .status-bar__right { font-weight: 400; }

  .brand { position: absolute; left: 0; width: 100%; text-align: center; }
  .brand__name {
    font-family: "Quicksand", sans-serif; font-weight: 400; font-size: 44px;
    letter-spacing: 18px; padding-left: 18px; line-height: 1;
  }
  .brand__tagline {
    position: absolute; left: 0; width: 100%; text-align: center;
    font-family: "Open Sans", sans-serif; font-size: 19px;
  }
  .screen--dark .brand__name, .screen--dark .brand__tagline { color: var(--white); }
  .screen--cyan .brand__name, .screen--cyan .brand__tagline { color: var(--ink); }

  .login-pill {
    position: absolute; left: 229px; top: 60px; width: 157px; height: 47px;
    background: var(--coral); border-radius: 6px 0 0 6px; display: flex; align-items: center;
    color: var(--white); font-family: "Quicksand", sans-serif; font-size: 19px;
  }
  .login-pill__icon {
    width: 48px; height: 100%; display: flex; align-items: center; justify-content: center;
    border-right: 1px solid rgba(255,255,255,0.3);
  }
  .login-pill__label { padding-left: 14px; }

  .action {
    position: absolute; display: flex; align-items: center;
    font-family: "Quicksand", sans-serif; color: var(--white);
  }
  .action--sky { left: 43px; width: 299px; height: 47px; background: var(--sky); border-radius: 5px; font-size: 16px; }
  .action--sky .action__icon {
    width: 50px; height: 100%; display: flex; align-items: center; justify-content: center;
    border-right: 1px solid rgba(255,255,255,0.3);
  }
  .action--sky .action__label { padding-left: 14px; }
  .action--black { background: var(--ink); font-size: 13px; }
  .action--black .action__icon { width: 40px; display: flex; align-items: center; justify-content: center; }
  .action--black .action__label { padding-left: 4px; }

  .login-bar {
    position: absolute; left: 0; top: 650px; width: 100%; height: 36px; background: var(--coral);
    display: flex; align-items: center; justify-content: center; gap: 10px;
    color: var(--white); font-family: "Quicksand", sans-serif; font-size: 16px;
  }

  .caption {
    position: absolute; font-family: "Montserrat", sans-serif; font-weight: 700;
    color: var(--white); white-space: nowrap;
  }
  .caption--mock { top: 1085px; font-size: 28px; letter-spacing: 0.5px; }
  .caption--one { left: 111px; }
  .caption--two { left: 705px; }
  .caption--spec { top: 1142px; left: 0; width: 1138px; text-align: center; font-size: 28px; }
</style>
</head>
<body>
  <div class="backdrop backdrop--left"></div>
  <div class="backdrop backdrop--right"></div>

  <!-- Mock 1: dark home screen -->
  <section class="screen screen--dark">
    <div class="status-bar">
      <span class="status-bar__left">●●●○○ Corvo
        <svg width="14" height="11" viewBox="0 0 14 11"><path d="M1 4a9 9 0 0 1 12 0M3 6.3a6 6 0 0 1 8 0M5 8.5a3 3 0 0 1 4 0" fill="none" stroke="#111" stroke-width="1.6"/><circle cx="7" cy="10" r="1" fill="#111"/></svg>
      </span>
      <span class="status-bar__time">4:21 PM</span>
      <span class="status-bar__right">100%
        <svg width="30" height="12" viewBox="0 0 30 12"><rect x="0.5" y="0.5" width="26" height="11" rx="2" fill="none" stroke="#111"/><rect x="2" y="2" width="23" height="8" fill="#111"/><rect x="27.5" y="4" width="2" height="4" fill="#111"/></svg>
      </span>
    </div>

    <div class="login-pill">
      <span class="login-pill__icon">
        <svg width="26" height="26" viewBox="0 0 26 26"><circle cx="13" cy="13" r="11" fill="none" stroke="#fff" stroke-width="2"/><path d="M7 13h11M14 9l4 4-4 4" fill="none" stroke="#fff" stroke-width="2"/></svg>
      </span>
      <span class="login-pill__label">Login</span>
    </div>

    <div class="brand" style="top:366px"><div class="brand__name">VAMO</div></div>
    <p class="brand__tagline" style="top:420px">Your private parking space</p>

    <a class="action action--sky" style="top:505px">
      <span class="action__icon">
        <svg width="28" height="28" viewBox="0 0 28 28"><path d="M3 10 14 3l11 7" fill="none" stroke="#fff" stroke-width="2.2"/><circle cx="14" cy="17" r="8" fill="#fff"/><text x="14" y="21.5" text-anchor="middle" font-family="Open Sans, sans-serif" font-size="12" font-weight="600" fill="#3aa8de">P</text></svg>
      </span>
      <span class="action__label">Lease your parking space</span>
    </a>
    <a class="action action--sky" style="top:563px">
      <span class="action__icon">
        <svg width="28" height="28" viewBox="0 0 28 28"><path d="M11 2a8 8 0 0 1 8 8c0 6-8 14-8 14S3 16 3 10a8 8 0 0 1 8-8z" fill="#fff"/><text x="11" y="14" text-anchor="middle" font-family="Open Sans, sans-serif" font-size="10" font-weight="600" fill="#3aa8de">P</text><circle cx="19" cy="19" r="4" fill="#fff" stroke="#3aa8de" stroke-width="1.5"/><path d="M22 22l4 4" stroke="#fff" stroke-width="2"/></svg>
      </span>
      <span class="action__label">Search for parking</span>
    </a>
  </section>

  <!-- Mock 2: cyan home screen -->
  <section class="screen screen--cyan">
    <div class="status-bar">
      <span class="status-bar__left">●●●○○ Corvo
        <svg width="14" height="11" viewBox="0 0 14 11"><path d="M1 4a9 9 0 0 1 12 0M3 6.3a6 6 0 0 1 8 0M5 8.5a3 3 0 0 1 4 0" fill="none" stroke="#111" stroke-width="1.6"/><circle cx="7" cy="10" r="1" fill="#111"/></svg>
      </span>
      <span class="status-bar__time">4:21 PM</span>
      <span class="status-bar__right">100%
        <svg width="30" height="12" viewBox="0 0 30 12"><rect x="0.5" y="0.5" width="26" height="11" rx="2" fill="none" stroke="#111"/><rect x="2" y="2" width="23" height="8" fill="#111"/><rect x="27.5" y="4" width="2" height="4" fill="#111"/></svg>
      </span>
    </div>

    <div class="brand" style="top:290px"><div class="brand__name">VAMO</div></div>
    <p class="brand__tagline" style="top:342px">Your private parking space</p>

    <a class="action action--black" style="left:81px; top:405px; width:223px; height:35px">
      <span class="action__icon">
        <svg width="24" height="24" viewBox="0 0 28 28"><path d="M3 10 14 3l11 7" fill="none" stroke="#fff" stroke-width="2.2"/><circle cx="14" cy="17" r="8" fill="#fff"/><text x="14" y="21.5" text-anchor="middle" font-family="Open Sans, sans-serif" font-size="12" font-weight="600" fill="#0d0d0f">P</text></svg>
      </span>
      <span class="action__label">Lease your parking space</span>
    </a>
    <a class="action action--black" style="left:95px; top:453px; width:198px; height:35px">
      <span class="action__icon">
        <svg width="24" height="24" viewBox="0 0 28 28"><path d="M11 2a8 8 0 0 1 8 8c0 6-8 14-8 14S3 16 3 10a8 8 0 0 1 8-8z" fill="#fff"/><text x="11" y="14" text-anchor="middle" font-family="Open Sans, sans-serif" font-size="10" font-weight="600" fill="#0d0d0f">P</text><circle cx="19" cy="19" r="4" fill="#fff" stroke="#0d0d0f" stroke-width="1.5"/><path d="M22 22l4 4" stroke="#fff" stroke-width="2"/></svg>
      </span>
      <span class="action__label">Search for parking</span>
    </a>

    <div class="login-bar">
      <svg width="22" height="20" viewBox="0 0 22 20"><path d="M8 4V1h13v18H8v-3" fill="none" stroke="#fff" stroke-width="1.6"/><path d="M1 10h13M10 6l4 4-4 4" fill="none" stroke="#fff" stroke-width="1.6"/></svg>
      <span>Login</span>
    </div>
  </section>

  <p class="caption caption--mock caption--one">Home Screen - mock 1</p>
  <p class="caption caption--mock caption--two">Home Screen - mock 2</p>
  <p class="caption caption--spec">Handset- Screen Dimension - 640 px X 1094 px (without top status bar)</p>
</body>
</html>
```